IT Consulting Firm Website
Core Values: Proficiency ♦ Consistency ♦ Integrity
IT Consulting Firm Website - Information Technology
Creative Brief
Information Technology
www.dunmorevantage.com
Premier IT Services Consulting firm with a heavy emphasis on ethical business practices and superior technical skillsets. Dunmore Consulting designs and implements effective solutions that are specific to the client's information technology issues and business model. Harness our ability to assess your information technology concerns and deliver a solution that meets the company's current requirements and plan appropriately for the company's future demands. DCHP understands how technology works and has a clear focus enabling us to accurately read the strategic big picture of any business challenge. Business continuity and disaster recovery plans are also addressed and implemented as part of the IT solution. Dunmore Consulting has led successful efforts in delivering effective IT solutions to difficult and complex business challenges.
we are looking for a website design that will establish our brand as professional, ethical and technically superior to our competitors. Nothing cartoonish. Something that will identify us by the solid and stable IT industry relationships we've developed.
Modern
Core color is Cobalt Blue (Pantone 288C - RGB 00337F)
RGB 1975FF
RGB 3F3F3F & RGB 000000
below header
Please use images from www.lumepixbank.com Also, please make sure you guys use our NEW logo that I've uploaded to the project and to design with that in mind. Not our old logo that you see on the website.

```html
<!DOCTYPE html>
<html lang="en">
<head>
<meta charset="utf-8">
<title>Dunmore Consulting Group</title>
<link rel="stylesheet" href="https://fonts.googleapis.com/css2?family=Arimo:wght@400;700&display=swap">
<style>
:root{
  --cobalt:#00337f;
  --bright:#1975ff;
  --ink:#3f3f3f;
  --black:#000;
  --page:#ececec;
  --panel:#fafafa;
  --line:#d2d2d2;
  --muted:#8a8a8a;
  --footer:#4a4a4a;
}
*{box-sizing:border-box;margin:0;padding:0}
html,body{width:1200px;height:901px;overflow:hidden}
body{font-family:"Arimo",Arial,sans-serif;color:var(--ink);background:linear-gradient(#f4f4f4,#e2e2e2 85%);position:relative}
.abs{position:absolute}
.brand{left:455px;top:34px;display:flex;align-items:center;gap:14px}
.brand-mark{width:70px;height:70px;border-radius:50%;background:var(--cobalt)}
.brand-name{color:var(--cobalt);font-weight:700;font-size:34px;line-height:1.05}
.brand-name small{display:block;font-size:22px}
.nav{left:309px;top:146px;width:582px;height:30px;border-bottom:1px solid var(--line);font-size:13px;color:var(--ink)}
.nav a{position:absolute;top:0;height:26px;line-height:26px;text-decoration:none;color:var(--ink)}
.nav .active{background:linear-gradient(#2f8bff,#0a4fc4);color:#fff;width:100px;text-align:center;border-radius:2px}
.nav .sep{position:absolute;top:6px;width:1px;height:14px;background:#bbb}
.hero{left:129px;top:190px;width:520px;height:265px;background:linear-gradient(120deg,#6a5a4d,#c9c4bd 55%,#8c98a6);border:1px solid #bbb}
.hero-caption{left:152px;top:372px;color:#fff}
.hero-caption h1{font-size:30px;font-weight:700;color:#5aa7ff}
.hero-caption p{font-size:15px}
.tab{top:190px;width:54px;height:265px;display:flex;align-items:flex-end;justify-content:center;padding-bottom:18px;font-size:18px;color:#fff;background:linear-gradient(90deg,#bdbdbd,#e8e8e8);border:1px solid #aaa}
.tab.on{background:linear-gradient(90deg,#0a4fc4,#2f8bff)}
.sidebar{left:842px;top:190px;width:229px;height:565px;background:var(--panel);box-shadow:0 0 6px rgba(0,0,0,.2);padding:18px 14px;font-size:12px}
.phone{display:flex;align-items:center;gap:8px;font-size:19px;color:var(--ink);padding-bottom:14px;border-bottom:1px solid var(--line)}
.sidebar .site{margin-top:14px;color:var(--ink)}
.sidebar .offices{margin-top:10px}
.sidebar .offices b{color:var(--bright);font-weight:400}
.sidebar .blurb{margin-top:28px;color:var(--cobalt);line-height:1.5}
.sidebar h3{color:var(--bright);font-size:13px;font-weight:700;margin-top:28px;padding-bottom:6px;border-bottom:1px solid var(--line)}
.social{display:flex;gap:8px;margin-top:10px}
.social span{width:20px;height:20px;border-radius:3px;background:#c9c9c9}
.field{margin-top:10px;height:26px;border:1px solid var(--line);background:#fff;font-size:10px;color:var(--muted);padding:6px 8px}
.field.msg{height:80px}
.submit{margin:12px 0 0 auto;width:86px;height:26px;background:linear-gradient(#fff,#d6d6d6);border:1px solid #bbb;font-size:11px;text-align:center;line-height:24px}
.service{top:480px;font-size:12px}
.service h2{height:29px;line-height:29px;padding-left:10px;color:#fff;font-size:16px;font-weight:400;background:linear-gradient(#2f8bff,#0a4fc4);border-radius:2px}
.service .pic{margin-top:12px;height:124px;border:1px solid #bbb}
.service ul{list-style:none;margin-top:8px;line-height:18px}
.service li::before{content:"\25B8  ";color:var(--bright)}
.service .more{margin:16px auto 0;width:100px;height:22px;line-height:20px;text-align:center;font-size:11px;border:1px solid #bbb;background:linear-gradient(#fff,#dcdcdc)}
.partners{left:0;top:774px;width:1200px;height:83px;background:#fff;display:flex;align-items:center;padding-left:129px;gap:44px}
.partners h4{color:var(--cobalt);font-size:24px;font-weight:400}
.partner{font-size:22px;font-weight:700;color:#555}
.badge{width:44px;height:44px;border-radius:50%;background:#d4d4d4}
.footer{left:0;top:857px;width:1200px;height:44px;background:linear-gradient(#5a5a5a,#3a3a3a);color:#ddd;font-size:11px;display:flex;align-items:center;justify-content:space-between;padding:0 129px}
</style>
</head>
<body>
<div class="abs brand"><span class="brand-mark"></span><div class="brand-name">Dunmore<small>Consulting Group</small></div></div>

<nav class="abs nav">
  <a class="active" style="left:0">HOME</a>
  <a style="left:124px">COMPANY</a><span class="sep" style="left:200px"></span>
  <a style="left:209px">SOLUTIONS</a><span class="sep" style="left:302px"></span>
  <a style="left:316px">PARTNERS &amp; CERTIFICATIONS</a><span class="sep" style="left:510px"></span>
  <a style="left:523px">CONTACT</a>
</nav>

<div class="abs hero" role="img" aria-label="Photo of a businesswoman working at an office desk"></div>
<div class="abs hero-caption"><h1>Welcome to Dunmore</h1><p>Nevada-based IT firm that delivers innovative IT solutions.</p></div>
<div class="abs tab on" style="left:646px;width:56px">1</div>
<div class="abs tab" style="left:706px">2</div>
<div class="abs tab" style="left:766px">3</div>

<aside class="abs sidebar">
  <div class="phone"><svg width="18" height="22" viewBox="0 0 18 22"><rect x="2" y="1" width="14" height="20" rx="2" fill="#555"/><rect x="4" y="4" width="10" height="9" fill="#ddd"/></svg>555-014-7010</div>
  <div class="site">www.dunmorevantage.com</div>
  <div class="offices">Offices in <b>Las Vegas &amp; Reno</b></div>
  <p class="blurb">Lorem Ipsum is simply text of the printing and type setting industry. Lorem</p>
  <h3>Follow us</h3>
  <div class="social"><span></span><span></span><span></span><span></span><span></span><span></span></div>
  <h3>Contact us</h3>
  <div class="field">Your name</div>
  <div class="field">Your e-mail</div>
  <div class="field msg">Your message</div>
  <div class="submit">Submit</div>
</aside>

<section class="abs service" style="left:129px;width:185px">
  <h2>Network integration</h2>
  <div class="pic" role="img" aria-label="Photo of business people applauding" style="background:linear-gradient(#7d6a5c,#cbbfb4)"></div>
  <ul><li>Infrastructure Analysis</li><li>Improved Scalability</li><li>Business Continuity</li></ul>
  <div class="more">Read More &gt;</div>
</section>
<section class="abs service" style="left:341px;width:177px">
  <h2>Managed IT services</h2>
  <div class="pic" role="img" aria-label="Photo of a hand using a computer mouse" style="background:linear-gradient(#5c6470,#c0c6cf)"></div>
  <ul><li>Network Performance</li><li>Data Storage &amp; Management</li><li>Security Monitoring</li></ul>
  <div class="more">Read More &gt;</div>
</section>
<section class="abs service" style="left:553px;width:267px">
  <h2>Virtualization &amp; cloud computing</h2>
  <div class="pic" role="img" aria-label="Photo of a hand drawing a network diagram" style="background:linear-gradient(#f2f4f8,#b9c3d2)"></div>
  <ul><li>Simplify IT Management</li><li>Optimized Operational Efficiency</li><li>IT Services On Demand</li></ul>
  <div class="more">Read More &gt;</div>
</section>

<div class="abs partners">
  <h4>Partners</h4>
  <span class="partner">Corvane</span>
  <span class="partner">Nimbrix</span>
  <span class="partner">Quadrelle</span>
  <span class="partner">Halvex</span>
  <span class="partner">Brenlo</span>
  <span class="badge"></span>
</div>

<footer class="abs footer">
  <span>© 2006-2011 Dunmore Consulting Group Inc.. All rights reserved.</span>
  <span>About Us &nbsp;|&nbsp; Contact Us &nbsp;|&nbsp; Privacy Policy &nbsp;|&nbsp; Terms of Use</span>
</footer>
</body>
</html>
```